Gentle Harbor Label

We need labels for a new brewery called "Gentle Harbor":

We need one label, that we can slightly change to suit the style of liquid. So far the beers are:
- XPA
- Pale ALe
- IPA
- Black Ale

We want creative, fun labels, nothing traditional. but appropriate to suit all international markets.

Design was promoted in LOGO & not in Design, so we got a lot of logo's but very little designs for bottles/cans.

Gentle Harbor Brewing

```html
<!DOCTYPE html>
<html lang="en">
<head>
<meta charset="utf-8">
<title>Gentle Harbor Brewing – IPA Label</title>
<link href="https://fonts.googleapis.com/css2?family=Cinzel+Decorative:wght@700&family=Oranienbaum&display=swap" rel="stylesheet">
<style>
  :root {
    --label-black: #231f20;
    --ink-white: #ffffff;
    --accent-red: #d71f3c;
  }
  html, body {
    margin: 0;
    padding: 0;
    width: 726px;
    height: 1200px;
    overflow: hidden;
    background: var(--label-black);
  }
  .label {
    position: relative;
    width: 726px;
    height: 1200px;
    background: var(--label-black);
    color: var(--ink-white);
    overflow: hidden;
  }
  .brand-name {
    position: absolute;
    margin: 0;
    font-family: "Cinzel Decorative", serif;
    font-weight: 700;
    line-height: 1;
    white-space: nowrap;
  }
  .brand-name--first {
    top: 122px;
    left: 0;
    width: 655px;
    text-align: right;
    font-size: 92px;
    letter-spacing: -1px;
  }
  .brand-name--second {
    top: 262px;
    left: 0;
    width: 652px;
    text-align: right;
    font-size: 78px;
  }
  .brand-name--brewing {
    top: 410px;
    left: 83px;
    font-size: 62px;
  }
  .hero-artwork {
    position: absolute;
    top: 461px;
    left: 107px;
    width: 521px;
    height: 314px;
  }
  .beer-style {
    position: absolute;
    top: 900px;
    left: 0;
    width: 726px;
    margin: 0;
    text-align: center;
    font-family: "Oranienbaum", serif;
    font-size: 108px;
    line-height: 1;
    color: var(--accent-red);
  }
  .bottle-facts {
    position: absolute;
    top: 1082px;
    left: 0;
    width: 726px;
    margin: 0;
    padding: 0;
    list-style: none;
    font-family: "Oranienbaum", serif;
    font-size: 42px;
    line-height: 1;
  }
  .bottle-facts li {
    position: absolute;
    top: 0;
    white-space: nowrap;
  }
  .bottle-facts .volume { left: 118px; }
  .bottle-facts .category { left: 287px; font-size: 46px; }
  .bottle-facts .strength { left: 521px; }
</style>
</head>
<body>
  <main class="label">
    <h1 class="brand-name brand-name--first">Gentle</h1>
    <p class="brand-name brand-name--second">Harbor</p>
    <p class="brand-name brand-name--brewing">Brewing</p>

    <svg class="hero-artwork" role="img" aria-label="Brewery emblem artwork in red on black" viewBox="0 0 521 314" xmlns="http://www.w3.org/2000/svg">
      <defs>
        <radialGradient id="emblemGlow" cx="50%" cy="55%" r="60%">
          <stop offset="0%" stop-color="#d71f3c" stop-opacity="0.55"/>
          <stop offset="100%" stop-color="#231f20" stop-opacity="0"/>
        </radialGradient>
      </defs>
      <rect width="521" height="314" fill="url(#emblemGlow)"/>
    </svg>

    <h2 class="beer-style">IPA</h2>

    <ul class="bottle-facts">
      <li class="volume">330ml</li>
      <li class="category">craft beer</li>
      <li class="strength">4,9% alc</li>
    </ul>
  </main>
</body>
</html>
```